American cannabis tech company business card design

Quillo.com is seeking a modern, professional, and brand-aligned business card that represents our company and its core values: Mission, Story, Values, and Impact. As an innovative cannabis company, we want a business card that is not only visually appealing but also serves as a representation of who we are and what we stand for.

Project Scope: Design a double-sided business card that integrates our brand identity and core values. Incorporate our key brand elements, ensuring a sleek and contemporary aesthetic. Visually reflect our core values (Mission, Story, Values, Impact) in a way that is engaging yet professional.

Target Market(s)

Vendors, third parties,

Contact Information for Business Card

Contact details (name, title, email, phone, website, etc.)

Font styles to use
Other font styles liked:
• Caslon, Centra

Colors

Designer to choose colors to be used in the design.

Requirements
Must have
• Quillo.com logo and branding A creative yet clean way to integrate our core values (Mission, Story, Values, Impact) Modern typography and a well-structured layout
Nice to have
• forest green, grey, white, black
Should not have
• references to marijuana, leafs, plants, or related product

```html
<!DOCTYPE html>
<html lang="en">
<head>
<meta charset="utf-8">
<title>Quillo Business Card</title>
<link href="https://fonts.googleapis.com/css2?family=Outfit:wght@400;500;600;700&display=swap" rel="stylesheet">
<style>
  :root {
    --stage: #979797;
    --forest: #1b3320;
    --forest-soft: #24402a;
    --cream: #f8f2e9;
    --sand: #e6d8c3;
    --ink: #1c2e1f;
    --white: #ffffff;
  }
  html, body {
    margin: 0;
    padding: 0;
    width: 1200px;
    height: 1000px;
    overflow: hidden;
    background: var(--stage);
    font-family: "Outfit", sans-serif;
  }
  .canvas {
    position: relative;
    width: 1200px;
    height: 1000px;
  }
  .card {
    position: absolute;
    left: 252px;
    width: 694px;
    height: 400px;
    border-radius: 26px;
    overflow: hidden;
  }
  .card--front {
    top: 60px;
    background: var(--forest);
  }
  .card--back {
    top: 490px;
    background: var(--cream);
  }
  .front-texture {
    position: absolute;
    inset: 0;
    background: linear-gradient(90deg, var(--forest) 0%, var(--forest-soft) 100%);
  }
  .brand-name {
    position: absolute;
    left: 0;
    right: 0;
    top: 176px;
    margin: 0;
    text-align: center;
    font-size: 46px;
    font-weight: 700;
    color: var(--cream);
    line-height: 1;
  }
  .core-values {
    position: absolute;
    left: 0;
    right: 0;
    top: 266px;
    margin: 0;
    text-align: center;
    font-size: 24px;
    font-weight: 600;
    line-height: 30px;
    color: var(--white);
  }
  .core-values__dot {
    padding: 0 6px;
    color: var(--sand);
  }
  .back-monogram {
    position: absolute;
    left: 340px;
    top: 48px;
    width: 380px;
    height: 320px;
    border-radius: 60px 0 0 40px;
    background: radial-gradient(ellipse at 60% 50%, var(--sand) 0%, rgba(230,216,195,0.6) 60%, rgba(230,216,195,0) 100%);
  }
  .contact {
    position: absolute;
    left: 68px;
    top: 160px;
    width: 230px;
    text-align: center;
    color: var(--ink);
  }
  .contact__name {
    margin: 0;
    font-size: 28px;
    font-weight: 600;
    line-height: 1.1;
  }
  .contact__title {
    margin: 2px 0 0;
    font-size: 18px;
    font-weight: 400;
  }
  .contact__divider {
    display: block;
    margin: 10px auto 8px;
  }
  .contact__line {
    margin: 0;
    font-size: 19px;
    line-height: 23px;
  }
</style>
</head>
<body>
<div class="canvas">
  <section class="card card--front">
    <div class="front-texture" role="img" aria-label="Repeating brand name pattern in dark green tones"></div>
    <h1 class="brand-name">Quillo</h1>
    <p class="core-values">Mission<span class="core-values__dot">·</span>Story<span class="core-values__dot">·</span>Values<span class="core-values__dot">·</span>Impact</p>
  </section>

  <section class="card card--back">
    <div class="back-monogram" role="img" aria-label="Large faint speckled brand monogram"></div>
    <div class="contact">
      <h2 class="contact__name">Daniel Hayes</h2>
      <p class="contact__title">Co-Founder &amp; CEO</p>
      <svg class="contact__divider" width="190" height="18" viewBox="0 0 190 18" aria-hidden="true">
        <line x1="0" y1="9" x2="52" y2="9" stroke="#1c2e1f" stroke-width="1.2"/>
        <line x1="136" y1="9" x2="188" y2="9" stroke="#1c2e1f" stroke-width="1.2"/>
        <rect x="63" y="1" width="9" height="16" rx="1.5" fill="#1c2e1f"/>
        <circle cx="67.5" cy="14.5" r="0.9" fill="#f8f2e9"/>
        <rect x="84" y="4" width="17" height="11" fill="#1c2e1f"/>
        <polyline points="84,4 92.5,11 101,4" fill="none" stroke="#f8f2e9" stroke-width="1"/>
        <circle cx="118" cy="9" r="7" fill="none" stroke="#1c2e1f" stroke-width="1.4"/>
        <ellipse cx="118" cy="9" rx="3" ry="7" fill="none" stroke="#1c2e1f" stroke-width="1.2"/>
        <line x1="111" y1="9" x2="125" y2="9" stroke="#1c2e1f" stroke-width="1.2"/>
        <line x1="112" y1="5.5" x2="124" y2="5.5" stroke="#1c2e1f" stroke-width="1"/>
        <line x1="112" y1="12.5" x2="124" y2="12.5" stroke="#1c2e1f" stroke-width="1"/>
      </svg>
      <p class="contact__line">(405) 555-0148</p>
      <p class="contact__line">name@quillo.com</p>
      <p class="contact__line">quillo.com</p>
    </div>
  </section>
</div>
</body>
</html>
```